Luxury Jewellery Brand Business Card design
A website will be needed shortly after so show your skills
Luxury Jewellery Brand Business Card design  - Jewelry
Creative Brief
Simple
Marcus Delvecky
Creative Director
47D Westbury mansions Westbury place london sw3k 2rt
marcus@lorvanemora.com
www.lorvanemora.com
The phone number provided is for design purpose only the real phone number will replace the temp at the end of the competition
tobiasgrell tobiasgrell
Hello all designers!! I have been very impressed with all the entries so far. I would like to see your best versions with colour . The colors I like are royal puple,racing green ,Red and an all white version . I like grey too but must be a dark grey ... have a go ... Thanks
#10 try it all with the filled in logo
#3 like the size of the logo
Thanks.Your the first to upload Could you possibly try the card using Logo lorvanemora_logo2_47729.jpg that I have uploaded ?
hi guys , Good luck with this one !!!! I am looking for interesting business cards !! simple but memorable!!! Excited to see what you guys come up with.....

```html
<!DOCTYPE html>
<html lang="en">
<head>
<meta charset="utf-8">
<title>Lorvane Mora — Business Card</title>
<link href="https://fonts.googleapis.com/css2?family=Marcellus&family=Jost:ital,wght@0,400;0,500;1,400&display=swap" rel="stylesheet">
<style>
  :root {
    --backdrop: #e4e2df;
    --card-white: #ffffff;
    --card-black: #141414;
    --pattern-tone: #2e2e2e;
    --ink: #2a2a2a;
    --ink-soft: #555555;
    --accent-text: #3a3a3a;
    --rule: #8a8a8a;
    --paper-shadow: rgba(0,0,0,0.18);
  }
  * { margin: 0; padding: 0; box-sizing: border-box; }
  html, body {
    width: 1200px; height: 901px; overflow: hidden;
    background: var(--backdrop);
  }
  .stage { position: relative; width: 1200px; height: 901px; }

  .card {
    position: absolute;
    width: 560px; height: 320px;
    box-shadow: 0 10px 28px var(--paper-shadow);
  }

  /* Back of card */
  .card-back {
    left: 70px; top: 90px;
    background: var(--card-black);
    overflow: hidden;
  }
  .card-back .pattern-area {
    position: absolute; inset: 0;
    background: linear-gradient(135deg, var(--card-black), var(--pattern-tone) 50%, var(--card-black));
  }
  .card-back .back-mark {
    position: absolute; left: 50%; top: 50%;
    transform: translate(-50%, -50%);
    display: flex; flex-direction: column; align-items: center; gap: 10px;
    background: var(--card-black);
    padding: 14px 18px;
  }
  .back-mark .mark-square {
    width: 34px; height: 34px; background: var(--card-white);
  }
  .back-mark .brand-name {
    font-family: "Marcellus", serif;
    font-size: 15px; letter-spacing: 3px;
    color: var(--card-white);
  }

  /* Front of card */
  .card-front {
    left: 570px; top: 470px;
    background: var(--card-white);
  }
  .card-front .brand-block {
    position: absolute; left: 0; right: 0; top: 46px;
    display: flex; flex-direction: column; align-items: center;
  }
  .brand-block .mark-square {
    width: 46px; height: 46px; background: var(--ink);
  }
  .brand-block .brand-name {
    margin-top: 12px;
    font-family: "Marcellus", serif;
    font-size: 36px; letter-spacing: 2px;
    color: var(--ink);
  }

  .person {
    position: absolute; right: 300px; top: 196px;
    text-align: right;
    font-family: "Jost", sans-serif;
  }
  .person .person-name {
    font-size: 15px; font-weight: 500; font-style: italic;
    color: var(--ink);
  }
  .person .person-title {
    font-size: 12px; font-style: italic;
    color: var(--ink-soft);
  }

  .divider {
    position: absolute; left: 282px; top: 192px;
    width: 1px; height: 100px; background: var(--rule);
  }

  .contact {
    position: absolute; left: 298px; top: 192px;
    font-family: "Jost", sans-serif;
    font-size: 11.5px; line-height: 15px;
    color: var(--accent-text);
    list-style: none;
  }
  .contact .address { margin-bottom: 3px; width: 230px; }
  .contact li { display: flex; align-items: center; gap: 6px; }
  .contact svg { width: 10px; height: 10px; flex: none; fill: var(--ink); }
</style>
</head>
<body>
<main class="stage">

  <section class="card card-back" aria-label="Business card, reverse side">
    <div class="pattern-area" role="img" aria-label="Repeating monogram pattern in grey on black"></div>
    <div class="back-mark">
      <span class="mark-square"></span>
      <span class="brand-name">LORVANE MORA</span>
    </div>
  </section>

  <section class="card card-front" aria-label="Business card, front side">
    <div class="brand-block">
      <span class="mark-square"></span>
      <span class="brand-name">LORVANE MORA</span>
    </div>

    <div class="person">
      <p class="person-name">Marcus Delvecky</p>
      <p class="person-title">Creative Director</p>
    </div>

    <span class="divider"></span>

    <ul class="contact">
      <li class="address">47D Westbury mansions Westbury place london sw3k 2rt</li>
      <li>
        <svg viewBox="0 0 10 10" aria-hidden="true"><path d="M1 3c0-1 1-2 4-2s4 1 4 2v1H7V3H3v1H1z M2 5h6l1 4H1z"/></svg>
        0044 208 415 3920
      </li>
      <li>
        <svg viewBox="0 0 10 10" aria-hidden="true"><path d="M3 0h4a1 1 0 0 1 1 1v8a1 1 0 0 1-1 1H3a1 1 0 0 1-1-1V1a1 1 0 0 1 1-1zm0 1.5v6h4v-6z"/></svg>
        0044 7712 845 093
      </li>
      <li>
        <svg viewBox="0 0 10 10" aria-hidden="true"><path d="M0 2h10v6H0z M0 2l5 3.5L10 2" stroke="#fff" stroke-width="0.8"/></svg>
        marcus@lorvanemora.com
      </li>
      <li>
        <svg viewBox="0 0 10 10" aria-hidden="true"><circle cx="5" cy="5" r="4.5"/><path d="M0.5 5h9M5 0.5v9" stroke="#fff" stroke-width="0.7"/></svg>
        www.lorvanemora.com
      </li>
    </ul>
  </section>

</main>
</body>
</html>
```